Feminine, flirty personal business Card Design

I need a new business card designed with my rebranded colors, personal pic and logo. It needs to be feminine without being girly. Since I work primarily virtually, address info can be omitted if it improves the design aesthetic. New tagline is "Your Partner in Success". Image from old biz card provided for information purposes only.

Target Market(s)

Online wellness/business coaches.

Industry/Entity Type

Business

Contact Information for Business Card

Tess Morvick, Head Technology Tamer
Email to use is tess@brookwaysvc.com
See image of old corporate style card for additional details

Font styles to use
Script

Requirements
Must have
• A fresh, feminine look and artistic aesthetic. Needs to appeal to my target demographic.
Nice to have
• Some type of embellishment to make it visually interesting.
Should not have
• Must not be linear and corporate looking.

```html
<!DOCTYPE html>
<html lang="en">
<head>
<meta charset="utf-8">
<title>Tess Morvick – Business Card</title>
<link rel="stylesheet" href="https://fonts.googleapis.com/css2?family=Great+Vibes&family=Questrial&display=swap">
<style>
  :root {
    --backdrop: #2b2b2b;
    --teal: #27bbb1;
    --teal-pale: #a9dedd;
    --teal-mist: #d6efef;
    --slate: #5f5f61;
    --ink: #3a3a3c;
    --coral: #ef8a72;
    --white: #ffffff;
  }
  * { margin: 0; padding: 0; box-sizing: border-box; }
  html, body { width: 1200px; height: 1177px; overflow: hidden; }
  body {
    background: var(--backdrop);
    font-family: "Questrial", "Century Gothic", sans-serif;
    color: var(--ink);
    position: relative;
  }
  .card {
    position: absolute;
    left: 244px;
    width: 716px;
    height: 418px;
    border-radius: 40px;
    overflow: hidden;
    background: var(--white);
  }
  .card--front { top: 131px; }
  .card--back {
    top: 669px;
    background: radial-gradient(ellipse at 50% 48%, #ffffff 0%, #ffffff 35%, var(--teal-mist) 100%);
  }
  .front-curves { position: absolute; inset: 0; }
  .portrait {
    position: absolute;
    left: 52px; top: 72px;
    width: 176px; height: 176px;
    border-radius: 50%;
    border: 5px solid var(--white);
    background: radial-gradient(circle at 50% 40%, #e9c9a3 0%, #cfa57a 40%, #7fcfc6 75%, #5fc1b8 100%);
  }
  .holder-name {
    position: absolute;
    left: 0; width: 306px; top: 252px;
    text-align: center;
    font-family: "Great Vibes", cursive;
    font-size: 50px;
    color: var(--white);
    line-height: 1;
  }
  .holder-title {
    position: absolute;
    left: 0; width: 306px; top: 318px;
    text-align: center;
    font-size: 15px;
    color: var(--white);
  }
  .brand-lockup {
    position: absolute;
    right: 48px; top: 56px;
    width: 260px;
    text-align: center;
  }
  .brand-name {
    display: flex; align-items: center; justify-content: center; gap: 10px;
    font-size: 27px;
    color: var(--slate);
    line-height: 1.1;
  }
  .brand-dot { width: 14px; height: 14px; border-radius: 50%; background: var(--teal); flex: none; }
  .tagline {
    margin-top: 30px;
    font-size: 10px;
    letter-spacing: 2.6px;
    color: var(--slate);
  }
  .contact {
    position: absolute;
    right: 36px; top: 176px;
    list-style: none;
    text-align: right;
    font-size: 15.5px;
    line-height: 1.3;
  }
  .contact li { display: flex; justify-content: flex-end; align-items: flex-start; gap: 12px; }
  .contact .icon {
    width: 18px; height: 18px; flex: none; margin-top: 2px;
  }
  .contact-address { margin-bottom: 12px; }
  .contact-phone { margin-bottom: 9px; }
  .contact-email { margin-top: 6px; margin-bottom: 10px; }
  .contact-web { font-size: 19px; padding-right: 0; }
  .back-brand {
    position: absolute;
    left: 0; right: 0; top: 170px;
    display: flex; align-items: center; justify-content: center; gap: 16px;
    font-size: 44px;
    color: var(--slate);
  }
  .back-brand .brand-dot { width: 22px; height: 22px; }
</style>
</head>
<body>

<section class="card card--front" aria-label="Business card front">
  <svg class="front-curves" viewBox="0 0 716 418" width="716" height="418" aria-hidden="true">
    <path d="M0 0 H300 C340 100 320 300 236 418 H0 Z" fill="var(--teal-pale)" transform="translate(44 0)"/>
    <path d="M0 0 H300 C340 100 320 300 236 418 H0 Z" fill="var(--slate)" transform="translate(20 0)"/>
    <path d="M0 0 H300 C340 100 320 300 236 418 H0 Z" fill="var(--teal)"/>
  </svg>

  <div class="portrait" role="img" aria-label="Portrait photo of Tess Morvick"></div>
  <p class="holder-name">Tess Morvick</p>
  <p class="holder-title">Head Technology Tamer</p>

  <div class="brand-lockup">
    <p class="brand-name"><span class="brand-dot"></span>Brookway Virtual Services</p>
    <p class="tagline">YOUR PARTNER IN SUCCESS</p>
  </div>

  <ul class="contact">
    <li class="contact-address">
      <span>Brookway Virtual Services 4418<br>Alder Hollow Road NE Marlow,<br>Oregon 97112 USA</span>
      <svg class="icon" viewBox="0 0 18 18"><path d="M9 1a5.5 5.5 0 0 0-5.5 5.5C3.5 11 9 17 9 17s5.5-6 5.5-10.5A5.5 5.5 0 0 0 9 1z" fill="var(--teal)"/><circle cx="9" cy="6.5" r="2" fill="#fff"/></svg>
    </li>
    <li class="contact-phone">
      <span>555.204.0193</span>
      <svg class="icon" viewBox="0 0 18 18"><circle cx="9" cy="9" r="9" fill="var(--teal)"/><rect x="5" y="7" width="8" height="6" rx="1" fill="#fff"/><rect x="6.5" y="4.5" width="5" height="3" fill="#fff"/></svg>
    </li>
    <li class="contact-phone">
      <span>555.318.6642</span>
      <svg class="icon" viewBox="0 0 18 18"><circle cx="9" cy="9" r="9" fill="var(--teal)"/><path d="M6 4.5l1.8 2.3-1 1.2a6 6 0 0 0 3.2 3.2l1.2-1 2.3 1.8-1 1.6C9 13.4 4.6 9 4.4 5.5z" fill="#fff"/></svg>
    </li>
    <li class="contact-email">
      <span>tess@brookwaysvc.com</span>
      <svg class="icon" viewBox="0 0 18 18"><circle cx="9" cy="9" r="9" fill="var(--teal)"/><rect x="4.5" y="6" width="9" height="6.5" fill="#fff"/><path d="M4.5 6l4.5 3.5L13.5 6" fill="none" stroke="var(--teal)" stroke-width="1"/></svg>
    </li>
    <li class="contact-web"><span>www.brookwayvirtualservices.com</span></li>
  </ul>
</section>

<section class="card card--back" aria-label="Business card back">
  <p class="back-brand"><span class="brand-dot"></span>Brookway Virtual Services</p>
</section>

</body>
</html>
```